Food Menu Design for Japanese Restaurant

Design a food menu for a high-end Japanese food restaurant. See attached detailed requirements file and menu items.

Industry/Entity Type

Restaurant

Colors

Designer to choose colors to be used in the design.

Requirements
Must have
• All menu items, descriptions, prices, add-ons, as provided in requirements file, all shown on designed menu and formatted.

```html
<!DOCTYPE html>
<html lang="en">
<head>
<meta charset="utf-8">
<title>Tazumi — Starters &amp; Soup</title>
<link rel="stylesheet" href="https://fonts.googleapis.com/css2?family=Archivo+Black&family=Roboto:ital,wght@0,100;0,400;0,700;1,400;1,700&display=swap">
<style>
  :root {
    --paper: #ffffff;
    --ink: #111111;
    --accent: #b3262a;
    --brand-grey: #6f6f6f;
    --leaf-tone: #e6e6e6;
  }
  * { margin: 0; padding: 0; box-sizing: border-box; }
  html, body { width: 1200px; height: 2400px; overflow: hidden; background: var(--paper); }
  .menu-page {
    position: relative;
    width: 1200px;
    height: 2400px;
    overflow: hidden;
    background: var(--paper);
    color: var(--ink);
    font-family: "Roboto", Arial, sans-serif;
  }
  .leaf-artwork {
    position: absolute;
    left: -60px;
    top: -40px;
    width: 1240px;
    height: 1800px;
    background:
      radial-gradient(ellipse 420px 700px at 330px 620px, var(--leaf-tone) 0%, rgba(230,230,230,0.55) 45%, rgba(255,255,255,0) 75%),
      radial-gradient(ellipse 520px 320px at 900px 220px, rgba(230,230,230,0.7) 0%, rgba(255,255,255,0) 70%),
      radial-gradient(ellipse 380px 420px at 760px 1250px, rgba(232,232,232,0.7) 0%, rgba(255,255,255,0) 70%);
  }
  .brand-name {
    position: absolute;
    left: 40px;
    top: 880px;
    display: flex;
    align-items: center;
    gap: 12px;
    font-family: "Roboto", Arial, sans-serif;
    font-weight: 400;
    font-size: 34px;
    line-height: 1;
    color: var(--brand-grey);
    white-space: nowrap;
  }
  .brand-mark {
    width: 14px;
    height: 14px;
    border-radius: 50%;
    background: var(--brand-grey);
  }
  .section-title {
    position: absolute;
    font-family: "Roboto", Arial, sans-serif;
    font-weight: 100;
    font-size: 82px;
    line-height: 1;
    letter-spacing: 0.13em;
    color: var(--accent);
  }
  .section-title--starters { left: 276px; top: 126px; }
  .section-title--soup { left: 296px; top: 1898px; }
  .section-divider {
    position: absolute;
    left: 210px;
    top: 1870px;
    width: 816px;
    height: 2px;
    background: var(--accent);
  }
  .item {
    position: absolute;
    left: 212px;
    width: 814px;
  }
  .item-name {
    font-family: "Archivo Black", "Arial Black", sans-serif;
    font-size: 24px;
    line-height: 28px;
    letter-spacing: 0.16em;
    text-transform: uppercase;
  }
  .item-line {
    display: flex;
    justify-content: space-between;
    align-items: baseline;
    padding-left: 24px;
    font-style: italic;
    font-size: 23px;
    line-height: 29px;
  }
  .item-line b { font-weight: 700; }
  .price {
    font-style: normal;
    font-weight: 700;
    font-size: 22px;
    color: var(--accent);
    min-width: 20px;
    text-align: right;
  }
  .portion-prices {
    text-align: right;
    font-style: italic;
    font-weight: 700;
    font-size: 23px;
    line-height: 38px;
  }
  .portion-prices .price { font-style: normal; }
</style>
</head>
<body>
<main class="menu-page">
  <div class="leaf-artwork" role="img" aria-label="Faint grey botanical illustration of large leaves and stems behind the menu"></div>

  <div class="brand-name"><span class="brand-mark"></span><span>Tazumi</span></div>

  <h1 class="section-title section-title--starters">STARTERS</h1>

  <section class="item" style="top:270px">
    <h2 class="item-name">Edamame</h2>
    <p class="item-line"><span><b>steamed:</b> soybeans, salted</span><span class="price">5</span></p>
    <p class="item-line"><span><b>spicy:</b> soybeans, sautéed with sesame oil &amp; sea salt</span><span class="price">6</span></p>
  </section>

  <section class="item" style="top:383px">
    <h2 class="item-name">Shishito Peppers</h2>
    <p class="item-line"><span>sautéed</span><span class="price">8</span></p>
  </section>

  <section class="item" style="top:465px">
    <h2 class="item-name">Agedashi Tofu</h2>
    <p class="item-line"><span>fried with scallions, bonito flakes, dashi sauce</span><span class="price">8</span></p>
  </section>

  <section class="item" style="top:547px">
    <h2 class="item-name">Spicy Rock Shrimp</h2>
    <p class="item-line"><span>tempura battered squid tossed with shichimi pepper powder,</span><span></span></p>
    <p class="item-line"><span>with spicy aioli sauce</span><span class="price">12</span></p>
  </section>

  <section class="item" style="top:660px">
    <h2 class="item-name">Shrimp Shumai</h2>
    <p class="item-line"><span>shrimp dumplings served steamed or deep fried</span><span></span></p>
    <p class="item-line"><span>with a seasoned soy dipping sauce</span><span class="price">7</span></p>
  </section>

  <section class="item" style="top:773px">
    <h2 class="item-name">Gyoza</h2>
    <p class="item-line"><span><b>pork:</b> Japanese dumplings with tofu, bean sprouts, chives</span><span></span></p>
    <p class="item-line"><span>steamed or deep fried</span><span class="price">8</span></p>
    <p class="item-line"><span><b>vegetable:</b> Japanese dumplings with shiitake mushrooms,</span><span></span></p>
    <p class="item-line"><span>spinach, leeks, edamame, steamed or deep fried</span><span class="price">7</span></p>
  </section>

  <section class="item" style="top:945px">
    <h2 class="item-name">Takoyaki</h2>
    <p class="item-line"><span>octopus dumplings with takoyaki sauce,</span><span></span></p>
    <p class="item-line"><span>Japanese mayonnaise, and bonito flakes</span><span class="price">6</span></p>
  </section>

  <section class="item" style="top:1058px">
    <h2 class="item-name">Tazumi Wings</h2>
    <p class="item-line"><span>chicken drummettes, spicy chili sauce, sesame seeds</span><span class="price">10</span></p>
  </section>

  <section class="item" style="top:1140px">
    <h2 class="item-name">Tuna Tartare</h2>
    <p class="item-line"><span>seasoned tuna served with cucumber slices, masago tuna</span><span class="price">14</span></p>
  </section>

  <section class="item" style="top:1222px">
    <p class="item-line" style="padding-left:0"><span class="item-name" style="font-style:normal">O Toro Tuna</span><span class="price">21</span></p>
  </section>

  <section class="item" style="top:1275px">
    <h2 class="item-name">Tuna Tataki</h2>
    <p class="item-line"><span>seared ahi tuna served with seaweed salad, ponzu</span><span class="price">13</span></p>
  </section>

  <section class="item" style="top:1358px">
    <h2 class="item-name">Soft Shell Crab</h2>
    <p class="item-line"><span>deep fried in light batter and served with ponzu dipping sauce</span><span class="price">9</span></p>
  </section>

  <section class="item" style="top:1441px">
    <h2 class="item-name">Carpaccio</h2>
    <p class="item-line"><span>lorem ipsum dolor sit amet, consectetur adipiscing elit</span><span class="price">X</span></p>
  </section>

  <section class="item" style="top:1524px">
    <h2 class="item-name">Oysters</h2>
    <p class="item-line"><span>“Tazumi” type oysters, raw, shucked and served on the half shell</span><span></span></p>
    <p class="portion-prices">1 dozen <span class="price">X</span> · 1/2 dozen <span class="price">X</span></p>
  </section>

  <section class="item" style="top:1647px">
    <h2 class="item-name">Chawanmushi</h2>
    <p class="item-line"><span>Lorem ipsum dolor sit amet, consectetur adipiscing elit</span><span class="price">X</span></p>
  </section>

  <section class="item" style="top:1730px">
    <h2 class="item-name">Shrimp &amp; Vegetable Tempura</h2>
    <p class="item-line"><span>shrimp &amp; seasonal vegetables fried tempura style</span><span class="price">11</span></p>
  </section>

  <div class="section-divider"></div>

  <h1 class="section-title section-title--soup">SOUP</h1>

  <section class="item" style="top:2030px">
    <h2 class="item-name">Miso Soup</h2>
    <p class="item-line"><span><b>original:</b> silken tofu and scallions in miso broth</span><span class="price">3</span></p>
    <p class="item-line"><span><b>Little neck clam miso:</b> Lorem ipsum dolor sit amet, consectetur</span><span class="price">X</span></p>
  </section>

  <section class="item" style="top:2143px">
    <h2 class="item-name">Dobin Mushi Pot Soup</h2>
    <p class="item-line"><span>lorem ipsum dolor sit amet, consectetur adipiscing elit</span><span class="price">X</span></p>
  </section>

  <section class="item" style="top:2227px">
    <h2 class="item-name">Kabocha Pumpkin Soup</h2>
    <p class="item-line"><span>creamy Asian pumpkin with a mild ginger aroma</span><span class="price">6</span></p>
  </section>
</main>
</body>
</html>
```